Design for web app with Plinkora Stratum Craft - Tarvo7 SMS consult

We are developing a web app that will work in browsers. Its main purpose is to allow for users (signing up and logging in with their phone number) to track their habbits and select consultants to whom they can send SMS for help.

The wireframes of the app can be accessed here (pdf):
https://files.plinkora.example/d/7K2mWqLzXv4NtRb9HcJpYsAeUfDg3/view

NB!: Please do not follow the mockups 100% literally, but the Plinkora Stratum craft guidelines.

The technical specifications and descriptions of the web app's functionalities are available in the link below:
https://papers.plinkora.example/doc/4HsTnV8bQeZr2LmXwYcKpDjAuFgN6oRiE5tW1yMx/edit

Requirements for the design:

- The design should be provided as PSD, where each page/section should be in its own PSD file OR all pages/sections should be represented as folder groups in a single PSD file.

- All graphical elements in the design should be delivered as single layers which can then be extracted from the PSD.

- All graphical elements (icons, graphical buttons, etc.) should be provided as vector objects in the PSD, so that they can be exported into different sizes without loss of quality (for responsiveness).

- The design should use either web safe fonts or Plinkora Type.

Instructions for the design:
The design should be based on Plinkora Stratum Craft - http://www.plinkora.example/craft/spec/stratum-craft/overview.html

Please also provide an app icon and suggest a logo for the app.

Requirements
Must have
• Based on Plinkora Stratum Craft
• Flat
Nice to have
• Nice looking and not so stiff as the default Plinkora Stratum Craft, but it is important to follow their guidelines.
Should not have
• 3D

```html
<!DOCTYPE html>
<html lang="en">
<head>
<meta charset="utf-8">
<title>Tarvo7 – Send SMS</title>
<link href="https://fonts.googleapis.com/css2?family=Roboto:wght@400;500&display=swap" rel="stylesheet">
<style>
  :root {
    --screen-bg: #01b3c9;
    --panel-bg: #0a93a6;
    --panel-edge: #4ec9d8;
    --status-bg: #dfe3e6;
    --status-ink: #1b1b1b;
    --ink-light: #ffffff;
    --field-bg: #ffffff;
    --field-ink: #444444;
    --send-top: #2bc41a;
    --send-bottom: #1ea70f;
    --cancel-top: #ff5656;
    --cancel-bottom: #ea3a3a;
  }
  * { box-sizing: border-box; margin: 0; padding: 0; }
  html, body {
    width: 1200px; height: 2322px; overflow: hidden;
    background: var(--screen-bg);
    font-family: "Roboto", Arial, sans-serif;
  }
  .app-screen { position: relative; width: 1200px; height: 2322px; background: var(--screen-bg); }

  .status-bar {
    position: absolute; left: 0; top: 0; width: 1200px; height: 62px;
    background: var(--status-bg); color: var(--status-ink);
    font-size: 38px; line-height: 62px;
  }
  .status-bar .carrier { position: absolute; left: 18px; top: 0; letter-spacing: 1px; }
  .status-bar .clock { position: absolute; left: 0; right: 0; text-align: center; }
  .status-bar .battery { position: absolute; right: 28px; top: 17px; }

  .brand {
    position: absolute; left: 78px; top: 140px;
    display: flex; align-items: center; gap: 18px;
  }
  .brand-mark { width: 30px; height: 30px; background: var(--ink-light); border-radius: 50%; }
  .brand-name { font-size: 60px; font-weight: 500; color: var(--ink-light); }

  .confirm-panel {
    position: absolute; left: 62px; top: 371px; width: 1088px; height: 1310px;
    background: var(--panel-bg); border: 3px solid var(--panel-edge);
    box-shadow: 0 4px 10px rgba(0,0,0,0.12);
  }
  .confirm-title {
    margin: 66px auto 0; width: 900px; text-align: center;
    color: var(--ink-light); font-size: 62px; font-weight: 500; line-height: 87px;
  }
  .sms-field {
    position: absolute; left: 84px; top: 429px; width: 916px; height: 458px;
    background: var(--field-bg); border: 2px solid #8fd3dc;
    padding: 44px 56px; font-family: inherit; font-size: 45px; color: var(--field-ink);
    resize: none; outline: none;
  }
  .sms-field::placeholder { color: var(--field-ink); }
  .action-button {
    position: absolute; left: 84px; width: 916px; height: 124px;
    border: none; border-radius: 8px; color: var(--ink-light);
    font-family: inherit; font-size: 50px; letter-spacing: 1px;
    box-shadow: 0 3px 6px rgba(0,0,0,0.18);
  }
  .action-send { top: 944px; background: linear-gradient(var(--send-top), var(--send-bottom)); }
  .action-cancel { top: 1109px; background: linear-gradient(var(--cancel-top), var(--cancel-bottom)); }
</style>
</head>
<body>
<main class="app-screen">
  <header class="status-bar">
    <span class="carrier">●●●○○ ABC</span>
    <span class="clock">10:38 AM</span>
    <svg class="battery" width="62" height="30" viewBox="0 0 62 30" aria-hidden="true">
      <rect x="1.5" y="1.5" width="52" height="27" rx="3" fill="none" stroke="#1b1b1b" stroke-width="3"/>
      <rect x="55" y="9" width="5" height="12" fill="#1b1b1b"/>
      <rect x="6" y="6" width="36" height="18" fill="#1b1b1b"/>
    </svg>
  </header>

  <div class="brand">
    <span class="brand-mark"></span>
    <span class="brand-name">Tarvo7</span>
  </div>

  <section class="confirm-panel">
    <h1 class="confirm-title">Please write the text for the SMS and confirm that you want to send it to</h1>
    <textarea class="sms-field" placeholder="SMS text"></textarea>
    <button class="action-button action-send">SEND</button>
    <button class="action-button action-cancel">CANCEL</button>
  </section>
</main>
</body>
</html>
```